TEK Logistics - Banner 2.5' x 8' for 20+ locations

Need a banner designed that will pop. This banner will be displayed at over 20 of our transportation facilities. Goal is for the banner to grab the attention of employees, contractors and clients and help reinforce our mission and core values. Designed needs to include TEK Logo, our core values and mission statement. Red and Black are the main company colors and we need to stay within that theme and color pallet. Attached is a previous version that was too basic and boring. Willing to consider a design that excludes the mission statement.

Gathering more feedback

```html
<!DOCTYPE html>
<html lang="en">
<head>
<meta charset="utf-8">
<title>TEK Logistics – Core Values Banner</title>
<link rel="stylesheet" href="https://fonts.googleapis.com/css2?family=Roboto:wght@500;700&display=swap">
<style>
  :root {
    --brand-red: #d42628;
    --brand-black: #262626;
    --ink: #1f1f1f;
    --paper: #ffffff;
    --backdrop: #e0e0e0;
    --placeholder: #d9d9d9;
  }
  html, body {
    margin: 0;
    width: 1200px;
    height: 1200px;
    overflow: hidden;
    background: var(--backdrop);
  }
  .banner {
    position: absolute;
    left: 79px;
    top: 405px;
    width: 1042px;
    height: 326px;
    background: var(--paper);
    overflow: hidden;
    font-family: "Roboto", Arial, sans-serif;
  }
  .banner-shapes {
    position: absolute;
    inset: 0;
  }
  .brand-name {
    position: absolute;
    left: 44px;
    top: 128px;
    color: var(--brand-red);
    font-weight: 700;
    line-height: 1;
  }
  .brand-name .brand-main {
    display: block;
    font-size: 44px;
    letter-spacing: 1px;
  }
  .brand-name .brand-sub {
    display: block;
    font-size: 15px;
    letter-spacing: 5px;
    margin-top: 3px;
  }
  .value {
    position: absolute;
    display: flex;
    align-items: center;
    gap: 0;
  }
  .value-icon {
    position: absolute;
    width: 44px;
    height: 44px;
    left: -80px;
    top: 50%;
    transform: translateY(-50%);
  }
  .icon-placeholder {
    border-radius: 50%;
    background: var(--placeholder);
  }
  .value-text {
    margin: 0;
    font-size: 16px;
    font-weight: 500;
    line-height: 19.5px;
    color: var(--ink);
    white-space: nowrap;
  }
  .mission {
    position: absolute;
    left: 240px;
    width: 770px;
    top: 264px;
    margin: 0;
    text-align: center;
    color: var(--paper);
    font-size: 17px;
    font-weight: 700;
    line-height: 20.5px;
    white-space: nowrap;
  }
</style>
</head>
<body>
  <main class="banner">
    <svg class="banner-shapes" width="1042" height="326" viewBox="0 0 1042 326" aria-hidden="true">
      <polygon points="751,0 1042,0 1042,12 763,12" fill="var(--brand-red)"/>
      <polygon points="778,12 1042,12 1042,19 784,19" fill="var(--brand-black)"/>
      <rect x="0" y="215" width="300" height="111" fill="var(--brand-red)"/>
      <rect x="0" y="256" width="1042" height="70" fill="var(--brand-red)"/>
      <rect x="264" y="249" width="778" height="7" fill="var(--brand-black)"/>
      <circle cx="129" cy="142" r="153" fill="var(--paper)"/>
    </svg>

    <div class="brand-name">
      <span class="brand-main">TEK</span>
      <span class="brand-sub">LOGISTICS</span>
    </div>

    <div class="value" style="left:449px; top:46px;">
      <div class="value-icon icon-placeholder" role="img" aria-label="Icon of a person with a check mark"></div>
      <p class="value-text">DO THE RIGHT THINGS<br>FOR THE RIGHT REASONS</p>
    </div>

    <div class="value" style="left:449px; top:117px;">
      <svg class="value-icon" viewBox="0 0 44 44" fill="none" stroke="var(--ink)" stroke-width="2" aria-hidden="true">
        <line x1="2" y1="41" x2="42" y2="41"/>
        <rect x="5" y="32" width="5" height="9"/>
        <rect x="14" y="28" width="5" height="13"/>
        <rect x="23" y="24" width="5" height="17"/>
        <rect x="32" y="18" width="5" height="23"/>
        <path d="M3 27 Q24 22 40 5"/>
        <polyline points="33,5 40,5 40,12"/>
      </svg>
      <p class="value-text">PURSUE GROWTH<br>AND DEVELOPMENT</p>
    </div>

    <div class="value" style="left:449px; top:186px;">
      <div class="value-icon icon-placeholder" role="img" aria-label="Icon of a team of people"></div>
      <p class="value-text">BUILD A POSITIVE<br>TEAM ATMOSPHERE</p>
    </div>

    <div class="value" style="left:782px; top:46px;">
      <svg class="value-icon" viewBox="0 0 48 44" fill="none" stroke="var(--ink)" stroke-width="2.4" aria-hidden="true">
        <rect x="18" y="6" width="27" height="26" rx="1"/>
        <path d="M18 14 H8 L3 22 V32 H18"/>
        <line x1="3" y1="22" x2="18" y2="22"/>
        <circle cx="10" cy="34" r="4" fill="var(--paper)"/>
        <circle cx="36" cy="34" r="4" fill="var(--paper)"/>
        <polyline points="26,19 30,23 38,14"/>
      </svg>
      <p class="value-text">DELIVER WOW<br>THROUGH SERVICE</p>
    </div>

    <div class="value" style="left:782px; top:115px;">
      <svg class="value-icon" viewBox="0 0 44 44" fill="none" stroke="var(--ink)" stroke-width="2.4" aria-hidden="true">
        <path d="M22 2 L38 8 V24 Q38 36 22 42 Q6 36 6 24 V8 Z"/>
        <polyline points="15,22 20,27 29,17"/>
      </svg>
      <p class="value-text">DO EVERYTHING<br>SAFELY</p>
    </div>

    <div class="value" style="left:782px; top:186px;">
      <div class="value-icon icon-placeholder" role="img" aria-label="Smiley icon"></div>
      <p class="value-text" style="line-height:39px;">HAVE FUN</p>
    </div>

    <p class="mission">PROVIDE THE BEST CUSTOMER EXPERIENCE WHILE CREATING AN ENVIRONMENT OF GROWTH AND<br>OPPORTUNITY FOR OUR CUSTOMERS, EMPLOYEES, AND SERVICE PROVIDERS</p>
  </main>
</body>
</html>
```